36" inch (height) x 96" inch (width) Banner for Baseball Field

Hello. This project is an advertisement that will be printed onto a 3 foot by 8 foot full color banner and placed at little league fields in Southern California. A theme of the banner can be baseball. The company is my law office practicing Estate Planning and Tax Law. I am uploading the current business card, which has the logo, website, and telephone number. You can also pull images from www.rkpembrove.com I would like the banner to be a fun design that incorporates baseball somehow, but draws attention to my law and tax office, and my website. Please be creative, and have fun with it. The colors of my practice are included in the logo. At the bottom, it should say "Attorney Advertisement," but this can be in very small font in the bottom right or left corner.

Target Market(s)

Youth Baseball Fans

Industry/Entity Type

Law; Accounting

Colors

Designer to choose colors to be used in the design.

Requirements
Must have
• My telephone number. My website.
Nice to have
• Would like to see "Estate Planning" and "Tax Law and Preparation" Would also like to see "Attorney" and "CPA" or "Certified Public Accountant" prominently diplayed

```html
<!DOCTYPE html>
<html lang="en">
<head>
<meta charset="utf-8">
<title>RK Pembrove – Attorney &amp; CPA Banner</title>
<link href="https://fonts.googleapis.com/css2?family=Cinzel:wght@400;600&family=Oswald:wght@500&family=Open+Sans:ital,wght@0,700;1,400&display=swap" rel="stylesheet">
<style>
  :root {
    --page: #e9ecef;
    --banner: #060606;
    --brand-blue: #1e8ad6;
    --band-blue: #2a86d0;
    --white: #ffffff;
    --grey-text: #a9a9ab;
    --ring: #2a2c31;
    --ring-light: #474a52;
  }
  html, body {
    margin: 0;
    padding: 0;
    width: 1200px;
    height: 1195px;
    overflow: hidden;
    background: var(--page);
  }
  .banner {
    position: absolute;
    left: 0;
    top: 372px;
    width: 1200px;
    height: 450px;
    background: var(--banner);
    overflow: hidden;
  }
  .firm {
    position: absolute;
    left: 0;
    top: 0;
    width: 410px;
    text-align: center;
  }
  .firm-mark {
    position: absolute;
    left: 161px;
    top: 57px;
  }
  .firm-offices {
    position: absolute;
    left: 0;
    width: 410px;
    top: 148px;
    font-family: "Cinzel", serif;
    font-size: 15px;
    letter-spacing: 1px;
    color: var(--grey-text);
  }
  .firm-of {
    position: absolute;
    left: 0;
    width: 410px;
    top: 166px;
    font-family: "Cinzel", serif;
    font-size: 8px;
    color: var(--brand-blue);
  }
  .firm-name {
    position: absolute;
    left: 0;
    width: 410px;
    top: 172px;
    font-family: "Cinzel", serif;
    font-weight: 400;
    font-size: 38px;
    line-height: 1.2;
    color: var(--brand-blue);
  }
  .credential-band {
    position: absolute;
    left: 0;
    top: 232px;
    width: 391px;
    height: 62px;
    background: linear-gradient(90deg, var(--band-blue) 0%, var(--band-blue) 65%, rgba(42,134,208,0.35) 100%);
  }
  .credential-band span {
    position: absolute;
    left: 0;
    width: 392px;
    top: 4px;
    text-align: center;
    font-family: "Oswald", sans-serif;
    font-weight: 500;
    font-size: 42px;
    line-height: 1.2;
    color: var(--white);
  }
  .feature {
    position: absolute;
    left: 440px;
    top: 0;
  }
  .services {
    position: absolute;
    right: 0;
    width: 300px;
    left: 903px;
    top: 80px;
    text-align: center;
    font-family: "Oswald", sans-serif;
    font-weight: 500;
    font-size: 46px;
    line-height: 61px;
    color: var(--brand-blue);
  }
  .services .plain { color: var(--white); }
  .contact {
    position: absolute;
    top: 344px;
    font-family: "Open Sans", sans-serif;
    font-weight: 700;
    font-size: 41px;
    line-height: 56px;
    color: var(--grey-text);
    white-space: nowrap;
  }
  .contact-web { left: 134px; }
  .contact-phone { left: 701px; }
  .contact svg { vertical-align: middle; margin-right: 10px; position: relative; top: -4px; }
  .disclaimer {
    position: absolute;
    right: 42px;
    bottom: 12px;
    font-family: "Open Sans", sans-serif;
    font-style: italic;
    font-size: 13px;
    color: var(--white);
  }
</style>
</head>
<body>
  <main class="banner">
    <svg class="feature" width="460" height="450" viewBox="0 0 460 450">
      <defs>
        <radialGradient id="night-field" cx="50%" cy="45%" r="55%">
          <stop offset="0%" stop-color="#e6ecf5"/>
          <stop offset="25%" stop-color="#7fa3cf"/>
          <stop offset="60%" stop-color="#1f3e73"/>
          <stop offset="100%" stop-color="#0a1226"/>
        </radialGradient>
      </defs>
      <circle cx="228" cy="210" r="196" fill="#0e0f12" stroke="var(--ring)" stroke-width="8"/>
      <path d="M 60 120 A 190 190 0 0 1 330 40" fill="none" stroke="var(--ring-light)" stroke-width="3"/>
      <path d="M 418 240 A 192 192 0 0 1 300 390" fill="none" stroke="var(--ring-light)" stroke-width="3"/>
      <circle cx="228" cy="206" r="168" fill="url(#night-field)" role="img" aria-label="Photo of a young batter in a blue jersey ready to swing under stadium lights at dusk"/>
    </svg>

    <section class="firm">
      <svg class="firm-mark" width="88" height="88" viewBox="0 0 88 88" aria-hidden="true">
        <circle cx="44" cy="44" r="40" fill="none" stroke="var(--brand-blue)" stroke-width="5"/>
      </svg>
      <div class="firm-offices">THE LAW OFFICES</div>
      <div class="firm-of">OF</div>
      <div class="firm-name">RK PEMBROVE</div>
    </section>

    <div class="credential-band"><span>Attorney &amp; CPA</span></div>

    <h2 class="services" style="margin:0;font-weight:500;">
      Estate Planning<br>
      Tax Law <span class="plain">and</span><br>
      Preparation
    </h2>

    <div class="contact contact-web">
      <svg width="44" height="44" viewBox="0 0 44 44" aria-hidden="true">
        <g fill="none" stroke="var(--brand-blue)" stroke-width="4">
          <circle cx="22" cy="22" r="19"/>
          <ellipse cx="22" cy="22" rx="8" ry="19"/>
          <line x1="3" y1="22" x2="41" y2="22"/>
          <line x1="6" y1="12" x2="38" y2="12"/>
          <line x1="6" y1="32" x2="38" y2="32"/>
        </g>
      </svg>www.rkpembrove.com
    </div>

    <div class="contact contact-phone">
      <svg width="34" height="40" viewBox="0 0 34 40" aria-hidden="true">
        <path d="M9 4 L14 12 L10 16 C12 23 16 28 22 31 L26 27 L33 33 L28 38 C15 36 4 22 3 9 Z" fill="none" stroke="var(--brand-blue)" stroke-width="3.5" stroke-linejoin="round"/>
        <path d="M20 6 A10 10 0 0 1 30 16 M20 12 A4 4 0 0 1 24 16" fill="none" stroke="var(--brand-blue)" stroke-width="2.5"/>
      </svg>(805) 555-0148
    </div>

    <div class="disclaimer">Attorney Advertisement</div>
  </main>
</body>
</html>
```